Bref créative
TORV stationery
Stationery
Simple
Marco Daniel Fervone Lusse de Telvin
Administrador
Rua das Acácias nº17 Luanda-Angola
marco.telvin@torv-exemplo.com
www.torv-exemplo.com

```html
<!DOCTYPE html>
<html lang="pt">
<head>
<meta charset="utf-8">
<title>TORV — Stationery</title>
<link href="https://fonts.googleapis.com/css2?family=Open+Sans:wght@400;700;800&display=swap" rel="stylesheet">
<style>
  :root{
    --blue:#1b6fb6;
    --blue-light:#4fa3dd;
    --orange:#f39a1e;
    --paper:#ffffff;
    --ground:#e9ecef;
    --ink:#5a6470;
    --faint:#dde9f4;
  }
  *{box-sizing:border-box;margin:0;padding:0}
  html,body{width:1200px;height:310px;overflow:hidden}
  body{background:var(--ground);font-family:"Open Sans",Arial,sans-serif;position:relative;color:var(--ink)}
  .piece{position:absolute;background:var(--paper);box-shadow:0 2px 6px rgba(0,0,0,.18);overflow:hidden}
  .piece svg.wave{position:absolute;left:0;width:100%}
  .brand{display:flex;align-items:center;gap:4px;font-weight:800;color:var(--blue);letter-spacing:.5px;line-height:1}
  .brand .mark{background:var(--orange);display:inline-block}
  .tiny{font-size:4px;line-height:1.35;color:var(--ink)}
  .watermark{position:absolute;font-weight:800;color:var(--faint);line-height:1}

  /* business cards */
  .card-front{left:12px;top:115px;width:132px;height:46px}
  .card-front .brand{position:absolute;left:10px;top:12px;font-size:18px}
  .card-front .brand .mark{width:14px;height:14px}
  .card-front .title{position:absolute;left:50px;top:30px}
  .card-back{left:149px;top:115px;width:115px;height:46px}
  .card-back .brand{position:absolute;right:8px;top:8px;font-size:11px}
  .card-back .brand .mark{width:9px;height:9px}
  .card-back .details{position:absolute;left:6px;top:24px;width:105px}
  .card-front-b{left:19px;top:206px;width:130px;height:48px}
  .card-front-b .brand{position:absolute;left:12px;top:14px;font-size:17px}
  .card-front-b .brand .mark{width:13px;height:13px}
  .card-back-b{left:156px;top:206px;width:113px;height:48px}
  .card-back-b .details{position:absolute;left:8px;top:8px}

  /* letterheads */
  .letterhead{top:19px;width:168px;height:245px}
  .letterhead.one{left:288px}
  .letterhead.two{left:492px}
  .letterhead .brand{position:absolute;left:14px;top:12px;font-size:12px}
  .letterhead .brand .mark{width:10px;height:10px}
  .letterhead .watermark{left:34px;top:96px;font-size:44px}
  .letterhead .footer{position:absolute;left:0;right:0;bottom:4px;text-align:center}
  .letterhead .head-info{position:absolute;right:12px;top:12px;text-align:right}

  /* envelopes */
  .env{width:192px}
  .env.dl{left:696px;top:48px;height:96px}
  .env.c5{left:696px;top:180px;height:84px}
  .env .brand{position:absolute;left:10px;top:10px;font-size:10px}
  .env .brand .mark{width:8px;height:8px}
  .env .return{position:absolute;left:10px;top:24px}
  .env-back{left:912px;top:48px;width:276px;height:96px}
  .env-front{left:912px;top:168px;width:276px;height:108px}
  .env-front .brand{position:absolute;left:22px;top:16px;font-size:10px}
  .env-front .brand .mark{width:8px;height:8px}
  .env-back .brand{position:absolute;left:130px;top:12px;font-size:8px}
  .env-back .brand .mark{width:7px;height:7px}
</style>
</head>
<body>

<!-- Business card, front -->
<div class="piece card-front">
  <svg class="wave" style="top:0;height:46px" viewBox="0 0 132 46" preserveAspectRatio="none">
    <path d="M100 0 Q112 23 100 46 L132 46 L132 0Z" fill="var(--blue)"/>
    <path d="M96 0 Q108 23 96 46" fill="none" stroke="var(--orange)" stroke-width="1.5"/>
  </svg>
  <div class="brand"><span class="mark"></span>TORV</div>
  <div class="tiny title">Administrador</div>
</div>

<!-- Business card, back -->
<div class="piece card-back">
  <svg class="wave" style="top:0;height:46px" viewBox="0 0 115 46" preserveAspectRatio="none">
    <path d="M0 0 L30 0 Q20 23 0 30Z" fill="var(--blue)"/>
    <path d="M0 33 Q22 25 34 0" fill="none" stroke="var(--orange)" stroke-width="1.2"/>
  </svg>
  <div class="brand"><span class="mark"></span>TORV</div>
  <div class="tiny details">
    <strong>Marco Daniel Fervone Lusse de Telvin</strong><br>
    Administrador<br>
    Rua das Acácias nº17 Luanda-Angola<br>
    marco.telvin@torv-exemplo.com
  </div>
</div>

<!-- Business card, front variant -->
<div class="piece card-front-b">
  <svg class="wave" style="bottom:0;height:48px" viewBox="0 0 130 48" preserveAspectRatio="none">
    <path d="M0 40 Q65 30 130 42 L130 48 L0 48Z" fill="var(--blue)"/>
    <path d="M0 38 Q65 28 130 40" fill="none" stroke="var(--orange)" stroke-width="1.2"/>
  </svg>
  <div class="brand"><span class="mark"></span>TORV</div>
</div>

<!-- Business card, back variant -->
<div class="piece card-back-b">
  <svg class="wave" style="bottom:0;height:48px" viewBox="0 0 113 48" preserveAspectRatio="none">
    <path d="M0 36 Q56 26 113 36 L113 48 L0 48Z" fill="var(--blue)"/>
    <path d="M0 34 Q56 24 113 34" fill="none" stroke="var(--orange)" stroke-width="1.2"/>
  </svg>
  <div class="tiny details">
    <strong>Marco Daniel Fervone Lusse de Telvin</strong><br>
    Administrador<br>
    www.torv-exemplo.com
  </div>
</div>

<!-- Letterhead, first page -->
<div class="piece letterhead one">
  <svg class="wave" style="bottom:0;height:30px" viewBox="0 0 168 30" preserveAspectRatio="none">
    <path d="M0 14 Q84 2 168 16 L168 30 L0 30Z" fill="var(--blue)"/>
    <path d="M0 11 Q84 -1 168 13" fill="none" stroke="var(--orange)" stroke-width="1.5"/>
  </svg>
  <div class="brand"><span class="mark"></span>TORV</div>
  <div class="tiny head-info">Rua das Acácias nº17<br>Luanda-Angola<br>www.torv-exemplo.com</div>
  <div class="watermark">TORV</div>
</div>

<!-- Letterhead, continuation -->
<div class="piece letterhead two">
  <svg class="wave" style="bottom:0;height:30px" viewBox="0 0 168 30" preserveAspectRatio="none">
    <path d="M0 14 Q84 2 168 16 L168 30 L0 30Z" fill="var(--blue)"/>
    <path d="M0 11 Q84 -1 168 13" fill="none" stroke="var(--orange)" stroke-width="1.5"/>
  </svg>
  <div class="watermark">TORV</div>
</div>

<!-- DL envelope -->
<div class="piece env dl">
  <svg class="wave" style="bottom:0;height:22px" viewBox="0 0 192 22" preserveAspectRatio="none">
    <path d="M0 10 Q96 0 192 12 L192 22 L0 22Z" fill="var(--blue)"/>
    <path d="M0 7 Q96 -3 192 9" fill="none" stroke="var(--orange)" stroke-width="1.2"/>
  </svg>
  <div class="brand"><span class="mark"></span>TORV</div>
  <div class="tiny return">Rua das Acácias nº17 Luanda-Angola</div>
</div>

<!-- C5 envelope -->
<div class="piece env c5">
  <svg class="wave" style="bottom:0;height:20px" viewBox="0 0 192 20" preserveAspectRatio="none">
    <path d="M0 9 Q96 0 192 11 L192 20 L0 20Z" fill="var(--blue)"/>
    <path d="M0 6 Q96 -3 192 8" fill="none" stroke="var(--orange)" stroke-width="1.2"/>
  </svg>
  <div class="brand"><span class="mark"></span>TORV</div>
</div>

<!-- Envelope, back with flap -->
<div class="piece env-back">
  <svg class="wave" style="top:0;height:96px" viewBox="0 0 276 96" preserveAspectRatio="none">
    <path d="M0 0 L276 0 L276 10 L150 46 Q138 50 126 46 L0 10Z" fill="var(--orange)"/>
    <path d="M0 96 L120 54 Q138 48 156 54 L276 96" fill="none" stroke="#d7dde3" stroke-width="1"/>
  </svg>
  <div class="brand"><span class="mark"></span>TORV</div>
</div>

<!-- Envelope, front -->
<div class="piece env-front">
  <svg class="wave" style="top:0;height:108px" viewBox="0 0 276 108" preserveAspectRatio="none">
    <path d="M0 0 L138 60 L276 0" fill="none" stroke="var(--blue-light)" stroke-width="1"/>
    <path d="M0 108 L120 56 M276 108 L156 56" fill="none" stroke="#d7dde3" stroke-width="1"/>
  </svg>
  <div class="brand"><span class="mark"></span>TORV</div>
</div>

</body>
</html>
```